Finance Product Agency Business Card Design

We're an agency that provides products (service contracts, gap insurance, tire and wheel, etc) and support to dealership finance departments. We specialize in training finance producers to maximize their potential and also keep them up to date on the ever changing compliance and legal landscape. I'll attach an image of our logo, excited to see what you all come up with. Would also be interested in discussing our new website design with the winner.

Target Market(s)

auto dealerships

Industry/Entity Type

Business

Contact Information for Business Card

Mark Dolvery
Phone 317.624.5583
Fax 855.472.3308
email Mark.Dolvery@brightlanecoverage.example

Requirements
Must have
• basic contact information
Nice to have
• looking for something professional but modern

```html
<!DOCTYPE html>
<html lang="en">
<head>
<meta charset="utf-8">
<title>Brightlane Coverage – Business Card</title>
<link rel="stylesheet" href="https://fonts.googleapis.com/css2?family=Oswald:wght@500;600&family=Rubik:wght@300;400&display=swap">
<style>
  :root {
    --backdrop: #a3a5a6;
    --card-white: #f7f7f5;
    --teal: #3e6373;
    --teal-dark: #33525f;
    --ink: #3a3f44;
    --on-teal: #ffffff;
  }
  * { box-sizing: border-box; margin: 0; padding: 0; }
  html, body { width: 1200px; height: 800px; overflow: hidden; }
  body {
    background: var(--backdrop);
    display: flex;
    flex-direction: column;
    align-items: center;
    justify-content: center;
    gap: 40px;
    font-family: "Rubik", sans-serif;
  }
  .card {
    width: 600px;
    height: 343px;
    position: relative;
    overflow: hidden;
    box-shadow: 0 6px 18px rgba(0,0,0,0.25);
  }
  /* Front */
  .card-front { background: var(--card-white); }
  .front-top {
    height: 52%;
    display: flex;
    align-items: center;
    justify-content: space-between;
    padding: 0 40px;
  }
  .brand {
    display: flex;
    align-items: center;
    gap: 12px;
  }
  .brand-dot {
    width: 30px; height: 30px;
    border-radius: 50%;
    background: var(--teal);
  }
  .brand-name {
    font-family: "Oswald", sans-serif;
    font-weight: 600;
    font-size: 26px;
    letter-spacing: 0.5px;
    text-transform: uppercase;
    color: var(--ink);
  }
  .holder-name {
    font-family: "Oswald", sans-serif;
    font-weight: 500;
    font-size: 34px;
    text-transform: uppercase;
    color: var(--ink);
    letter-spacing: 0.5px;
  }
  .front-band {
    height: 48%;
    background: linear-gradient(120deg, var(--teal-dark), var(--teal) 55%, #4a7181);
    padding: 26px 40px;
    display: flex;
    flex-direction: column;
    gap: 10px;
  }
  .contact-line {
    display: flex;
    align-items: center;
    gap: 18px;
    color: var(--on-teal);
    font-size: 19px;
    font-weight: 300;
    letter-spacing: 0.3px;
  }
  .contact-line svg { width: 20px; height: 20px; flex: none; }
  /* Back */
  .card-back {
    background: linear-gradient(120deg, var(--teal-dark), var(--teal) 55%, #4a7181);
    display: flex;
    align-items: center;
    justify-content: center;
  }
  .card-back .brand-dot { width: 44px; height: 44px; background: var(--on-teal); }
  .card-back .brand-name { font-size: 40px; color: var(--on-teal); }
  .card-back .brand { gap: 18px; }
</style>
</head>
<body>
  <article class="card card-front">
    <header class="front-top">
      <div class="brand">
        <span class="brand-dot"></span>
        <span class="brand-name">Brightlane Coverage</span>
      </div>
      <h1 class="holder-name">Mark Dolvery</h1>
    </header>
    <section class="front-band">
      <p class="contact-line">
        <svg viewBox="0 0 24 24" aria-label="Phone"><path fill="#fff" d="M6.6 10.8a15.1 15.1 0 0 0 6.6 6.6l2.2-2.2a1 1 0 0 1 1-.25 11.4 11.4 0 0 0 3.6.57 1 1 0 0 1 1 1V20a1 1 0 0 1-1 1A17 17 0 0 1 3 4a1 1 0 0 1 1-1h3.5a1 1 0 0 1 1 1c0 1.25.2 2.45.57 3.57a1 1 0 0 1-.25 1z"/></svg>
        317.624.5583
      </p>
      <p class="contact-line">
        <svg viewBox="0 0 24 24" aria-label="Fax"><path fill="#fff" d="M7 3h10v4H7zM4 8h16a2 2 0 0 1 2 2v6h-4v5H6v-5H2v-6a2 2 0 0 1 2-2zm4 8v3h8v-3z"/></svg>
        855.472.3308
      </p>
      <p class="contact-line">
        <svg viewBox="0 0 24 24" aria-label="Email"><path fill="#fff" d="M3 6h18v12H3zm2 2v.3l7 4.7 7-4.7V8l-7 4.5z"/></svg>
        Mark.Dolvery@brightlanecoverage.example
      </p>
    </section>
  </article>

  <article class="card card-back">
    <div class="brand">
      <span class="brand-dot"></span>
      <span class="brand-name">Brightlane Coverage</span>
    </div>
  </article>
</body>
</html>
```